Company presentation powerpoint template

Hello,
We are a cloud computing solution who focus to provide complete cloud solution for enterprise. We need a PPT template to introduce our company and solution. Our website is http://www.lumaversa.com, it would be great if the design will match our website style.
Industry/Entity Type
It Company

```html
<!DOCTYPE html>
<html lang="en">
<head>
<meta charset="utf-8">
<title>Lumaversa — Presentation Title</title>
<link href="https://fonts.googleapis.com/css2?family=League+Gothic&display=swap" rel="stylesheet">
<style>
  :root {
    --sky-white: #ffffff;
    --sky-pale: #d6f0fb;
    --sky-light: #8fd3f2;
    --sky-mid: #3db8ea;
    --sky-deep: #00a5e3;
    --horizon-line: #7ccff1;
    --brand-blue: #17a3df;
  }
  html, body {
    margin: 0;
    padding: 0;
    width: 1200px;
    height: 900px;
    overflow: hidden;
  }
  .slide {
    position: relative;
    width: 1200px;
    height: 900px;
    overflow: hidden;
    background: linear-gradient(
      to bottom,
      var(--sky-white) 0,
      var(--sky-white) 400px,
      var(--sky-pale) 425px,
      var(--sky-light) 445px,
      var(--sky-mid) 520px,
      var(--sky-deep) 600px,
      var(--sky-deep) 900px
    );
  }
  .horizon {
    position: absolute;
    left: 0;
    top: 440px;
    width: 1200px;
    height: 2px;
    background: var(--horizon-line);
  }
  .brand {
    position: absolute;
    left: 78px;
    top: 372px;
    display: flex;
    align-items: center;
    gap: 16px;
  }
  .brand-dot {
    width: 46px;
    height: 46px;
    border-radius: 50%;
    background: var(--brand-blue);
  }
  .brand-name {
    font-family: "League Gothic", "Arial Narrow", sans-serif;
    font-size: 76px;
    line-height: 1;
    color: var(--brand-blue);
    letter-spacing: 1px;
  }
  .slide-title {
    position: absolute;
    left: 526px;
    top: 345px;
    margin: 0;
    font-family: "League Gothic", "Arial Narrow", sans-serif;
    font-weight: 400;
    font-size: 116px;
    line-height: 1;
    letter-spacing: 1px;
    color: var(--brand-blue);
    white-space: nowrap;
  }
</style>
</head>
<body>
  <main class="slide">
    <div class="horizon"></div>
    <div class="brand">
      <span class="brand-dot"></span>
      <span class="brand-name">Lumaversa</span>
    </div>
    <h1 class="slide-title">PRESENTATION TITLE</h1>
  </main>
</body>
</html>
```